Bookcover: Lessons From the Silent Orchard

I am publishing a super-low-cost innovation book for €4,99 on Bravolo Self Release to help everyone become a great innovator: young ambitious people without college education nor a big budget. Do you want to help me?

Brief:
Design a book cover 1600 x 2560 pixels for BSR.
Main title: Lessons From the Silent Orchard
Sub title: mindset - insights - skills & tools
Author: Maarten de Klerk
Design: captive, and appealing to everyone
Target Group: young ambitious people without college education

For bravolo please format the height/width ratio of 1.6:1

```html
<!DOCTYPE html>
<html lang="en">
<head>
<meta charset="UTF-8">
<title>Lessons From the Silent Orchard — Maarten de Klerk</title>
<link rel="stylesheet" href="https://fonts.googleapis.com/css2?family=Anton&family=Barlow+Semi+Condensed:wght@700&family=Oswald:wght@700&display=swap">
<style>
  :root {
    --paper-light: #f7f8f9;
    --paper-mid: #eceef0;
    --paper-dark: #e2e5e8;
    --ink: #000000;
    --bronze: #b08457;
  }
  html, body {
    margin: 0;
    padding: 0;
    width: 750px;
    height: 1200px;
    overflow: hidden;
  }
  .cover {
    position: relative;
    width: 750px;
    height: 1200px;
    overflow: hidden;
    background: radial-gradient(ellipse at 20% 25%, var(--paper-light) 0%, var(--paper-mid) 55%, var(--paper-dark) 100%);
  }
  .cover-art {
    position: absolute;
    left: 288px;
    top: 50px;
    width: 432px;
    height: 520px;
    border-radius: 48% 52% 30% 40% / 45% 45% 30% 30%;
    background:
      radial-gradient(circle at 35% 30%, #c89a8a 0%, transparent 40%),
      radial-gradient(circle at 70% 60%, #c8b48e 0%, transparent 45%),
      radial-gradient(circle at 50% 80%, #5a6f8a 0%, transparent 40%),
      linear-gradient(160deg, #d8c9ad 0%, #b99a7c 50%, #8c6f6a 100%);
    opacity: 0.9;
  }
  .title {
    position: absolute;
    left: 78px;
    top: 248px;
    margin: 0;
    font-family: "Anton", "Oswald", sans-serif;
    font-weight: 400;
    font-size: 128px;
    line-height: 132px;
    letter-spacing: 1px;
    text-transform: uppercase;
    color: var(--ink);
  }
  .title-line { display: block; }
  .tagline {
    position: absolute;
    left: 79px;
    top: 918px;
    width: 594px;
    height: 82px;
    border-top: 4px solid var(--bronze);
    border-bottom: 4px solid var(--bronze);
    box-sizing: border-box;
    display: flex;
    justify-content: space-between;
    align-items: center;
    font-family: "Oswald", sans-serif;
    font-weight: 700;
    font-size: 38px;
    text-transform: uppercase;
    color: var(--ink);
  }
  .tagline .sep { color: var(--bronze); }
  .author {
    position: absolute;
    left: 76px;
    top: 1052px;
    margin: 0;
    font-family: "Barlow Semi Condensed", sans-serif;
    font-weight: 700;
    font-size: 88px;
    line-height: 1;
    color: var(--bronze);
  }
</style>
</head>
<body>
  <main class="cover">
    <div class="cover-art" role="img" aria-label="Sculpture of a human head in profile built from stacked colourful books"></div>
    <h1 class="title">
      <span class="title-line">Lessons</span>
      <span class="title-line">From</span>
      <span class="title-line">The</span>
      <span class="title-line">Silent</span>
      <span class="title-line">Orchard</span>
    </h1>
    <p class="tagline">
      <span>Mindset</span><span class="sep">•</span><span>Insights</span><span class="sep">•</span><span>Skills <span class="sep">&amp;</span> Tools</span>
    </p>
    <p class="author">Maarten de Klerk</p>
  </main>
</body>
</html>
```